We are having a Bright Dawn, Bold Self Reshape Challenge at our fitness studio. We need a poster design using the template attached as a reference. I have also included our Vorabloom logo to put on the poster. Please DO NOT use the graphics in the flyer as we are expecting something much better :-)

-Size needed 11x17 with bleeding for printing

-We need this made in Photoshop (CS3 friendly) or at least delivered in PS as we might change some text or re-arrange the design later on.

-We need this in layers.

```html
<!DOCTYPE html>
<html lang="en">
<head>
<meta charset="utf-8">
<title>Bright Dawn, Bold Self Reshape Challenge</title>
<link rel="stylesheet" href="https://fonts.googleapis.com/css2?family=Oswald:wght@500;700&family=Poppins:wght@400;600&display=swap">
<style>
  :root {
    --backdrop: #e9e6e1;
    --board: #2a2a2a;
    --board-edge: #1f1f1f;
    --chalk: #c9c9c9;
    --chalk-bright: #ffffff;
    --chalk-dim: #3a3a3a;
    --ornament-hi: #4a4a4a;
    --ornament-lo: #353535;
    --accent-blue: #3f88cf;
    --accent-orange: #d9873a;
  }
  * { margin: 0; padding: 0; box-sizing: border-box; }
  html, body { width: 899px; height: 1200px; overflow: hidden; }
  body { background: var(--backdrop); position: relative; font-family: "Poppins", sans-serif; }

  .poster {
    position: absolute; left: 150px; top: 137px; width: 600px; height: 926px;
    background: radial-gradient(ellipse at 50% 40%, #333 0%, var(--board) 55%, var(--board-edge) 100%);
    color: var(--chalk);
  }
  .poster > * { position: absolute; }

  .frame { left: 0; top: 0; width: 600px; height: 926px; }

  .ornament {
    background: radial-gradient(ellipse at center, var(--ornament-hi) 0%, var(--ornament-lo) 60%, transparent 100%);
    border-radius: 12px;
  }
  .ornament-title { left: 45px; top: 150px; width: 510px; height: 210px; }
  .ornament-tape { left: 75px; top: 543px; width: 450px; height: 122px; }
  .ornament-prize { left: 70px; top: 700px; width: 460px; height: 155px; }

  .brand {
    left: 0; width: 600px; top: 82px; text-align: center;
    font-family: "Oswald", sans-serif; font-weight: 700; font-size: 40px;
    letter-spacing: 2px; color: var(--chalk-bright); line-height: 1;
  }

  .headline { left: 0; width: 600px; text-align: center; font-family: "Oswald", sans-serif; font-weight: 700; line-height: 1; }
  .headline-top { top: 198px; font-size: 36px; color: var(--chalk); }
  .headline-main { top: 236px; font-size: 52px; color: #d6d6d6; letter-spacing: 1px; }
  .headline-sub { top: 298px; font-size: 15px; font-weight: 500; color: var(--chalk); letter-spacing: 0.5px; line-height: 1.2; }

  .duration {
    left: 0; width: 600px; top: 390px; text-align: center;
    font-weight: 600; font-size: 48px; color: var(--accent-blue); line-height: 1; letter-spacing: -0.5px;
    display: flex; justify-content: center; align-items: center; gap: 8px;
  }
  .duration-badge {
    display: inline-flex; align-items: center; justify-content: center;
    width: 42px; height: 42px; border-radius: 50%;
    border: 4px solid var(--accent-orange); color: var(--accent-orange);
    font-size: 24px; font-weight: 600;
  }
  .duration-note {
    left: 0; width: 600px; top: 444px; text-align: center;
    font-size: 10.5px; font-weight: 600; color: var(--accent-blue); letter-spacing: 0.2px;
  }

  .schedule { left: 0; width: 600px; top: 474px; text-align: center; }
  .schedule-item { margin-bottom: 5px; line-height: 1.15; }
  .schedule-label { color: var(--accent-orange); font-size: 12px; text-transform: uppercase; }
  .schedule-date { color: var(--chalk-bright); font-size: 14px; }

  .offer {
    left: 0; width: 600px; top: 605px; text-align: center;
    font-family: "Oswald", sans-serif; font-weight: 700; font-size: 21px;
    line-height: 1.2; color: #e2e2e2; letter-spacing: 0.3px;
  }

  .prize { left: 0; width: 600px; top: 728px; text-align: center; font-family: "Oswald", sans-serif; }
  .prize-amount { font-size: 70px; font-weight: 700; color: var(--chalk); line-height: 1; }
  .prize-note { font-family: "Poppins", sans-serif; font-size: 12px; font-weight: 600; color: var(--chalk); margin-top: 4px; }

  .footer {
    left: 0; width: 600px; top: 884px; text-align: center;
    font-size: 17px; color: var(--chalk-bright);
  }
  .footer strong { font-weight: 600; }
</style>
</head>
<body>
  <main class="poster">
    <svg class="frame" viewBox="0 0 600 926" aria-hidden="true">
      <g fill="none" stroke="#d8d8d8" stroke-width="2">
        <polyline points="55,248 25,248 25,896 75,896"/>
        <polyline points="545,248 575,248 575,896 530,896"/>
      </g>
    </svg>

    <div class="ornament ornament-title" role="img" aria-label="Chalk-drawn scrollwork crest with a ribbon banner behind the headline"></div>
    <div class="ornament ornament-tape" role="img" aria-label="Chalk-drawn measuring tape curling into a banner"></div>
    <div class="ornament ornament-prize" role="img" aria-label="Chalk-drawn floral flourish framing the prize"></div>

    <div class="brand">VORABLOOM BOOTCAMPS</div>

    <h1 class="headline headline-top">BRIGHT DAWN</h1>
    <div class="headline headline-main">BOLD SELF</div>
    <div class="headline headline-sub">RESHAPE<br>CHALLENGE</div>

    <div class="duration">IN JUST <span class="duration-badge">6</span> WEEKS</div>
    <div class="duration-note">TRANSFORM YOUR BODY AND GET IN THE BEST SHAPE OF YOUR LIFE!</div>

    <div class="schedule">
      <div class="schedule-item"><div class="schedule-label">Kick off meeting</div><div class="schedule-date">Thursday, Jan 14 at 7:30pm</div></div>
      <div class="schedule-item"><div class="schedule-label">Start date</div><div class="schedule-date">Monday, January 18th</div></div>
      <div class="schedule-item"><div class="schedule-label">End date</div><div class="schedule-date">Friday, February 26th</div></div>
    </div>

    <div class="offer">6 WEEKS OF TRAINING, NUTRITION, AND<br>COACHING STARTING AT JUST $99!</div>

    <div class="prize">
      <div class="prize-amount">$500</div>
      <div class="prize-note">CASH PRIZE FOR WINNER!</div>
    </div>

    <div class="footer">visit www.<strong>vorabloombootcamps</strong>.com for more info</div>
  </main>
</body>
</html>
```